Building Company Business Card Design

I am looking to get a business card designed for my Building Company. Please find the logo attached.

Industry/Entity Type

Business

Contact Information for Business Card

Mobile 0472 913 706
Email admin@harbourlineconstruct.com.au
Website www.harbourlineconstruct.com.au

Colors
0255a3

```html
<!DOCTYPE html>
<html lang="en">
<head>
<meta charset="utf-8">
<title>Harbourline Construct – Business Card</title>
<link rel="stylesheet" href="https://fonts.googleapis.com/css2?family=Open+Sans:wght@400;600&family=Oswald:wght@500&display=swap">
<style>
  :root {
    --backdrop: #ebe8e4;
    --card-dark: #232323;
    --card-light: #ffffff;
    --brand-blue: #0255a3;
    --mark-grey: #8a8a8a;
    --text-grey: #3d3d3d;
    --shadow: 0 6px 18px rgba(0, 0, 0, 0.18);
  }
  * { margin: 0; padding: 0; box-sizing: border-box; }
  html, body {
    width: 1200px;
    height: 1000px;
    overflow: hidden;
    background: var(--backdrop);
    font-family: "Open Sans", Arial, sans-serif;
  }
  .card {
    position: absolute;
    left: 266px;
    width: 666px;
    border-radius: 28px;
    box-shadow: var(--shadow);
  }
  .card--front {
    top: 75px;
    height: 395px;
    background: var(--card-dark);
    display: flex;
    align-items: center;
    justify-content: center;
  }
  .brand-name {
    font-family: "Open Sans", Arial, sans-serif;
    font-weight: 600;
    font-size: 38px;
    letter-spacing: 1px;
    color: var(--mark-grey);
  }
  .card--back {
    top: 533px;
    height: 397px;
    background: var(--card-light);
  }
  .identity {
    position: absolute;
    right: 401px;
    top: 168px;
    text-align: right;
  }
  .person-name {
    font-family: "Oswald", "Arial Narrow", sans-serif;
    font-weight: 500;
    font-size: 25px;
    line-height: 30px;
    color: var(--brand-blue);
    letter-spacing: 0.3px;
  }
  .person-role {
    font-size: 16px;
    line-height: 26px;
    color: var(--text-grey);
  }
  .divider {
    position: absolute;
    left: 281px;
    top: 169px;
    width: 2px;
    height: 63px;
    background: var(--brand-blue);
  }
  .contact-list {
    position: absolute;
    left: 299px;
    top: 161px;
    list-style: none;
  }
  .contact-item {
    display: flex;
    align-items: center;
    gap: 7px;
    font-size: 16px;
    line-height: 24px;
    color: var(--text-grey);
  }
  .contact-icon {
    width: 14px;
    height: 14px;
    fill: var(--brand-blue);
    flex: none;
  }
  .address-line {
    position: absolute;
    left: 0;
    right: 0;
    top: 348px;
    text-align: center;
    font-size: 16px;
    color: var(--text-grey);
  }
  .address-line .company {
    color: var(--brand-blue);
  }
</style>
</head>
<body>
  <section class="card card--front">
    <span class="brand-name">HARBOURLINE CONSTRUCT</span>
  </section>

  <section class="card card--back">
    <div class="identity">
      <p class="person-name">CALLUM REYES</p>
      <p class="person-role">Managing Director</p>
    </div>
    <div class="divider"></div>
    <ul class="contact-list">
      <li class="contact-item">
        <svg class="contact-icon" viewBox="0 0 16 16" aria-hidden="true"><path d="M1 5c0-2 3-3 7-3s7 1 7 3v1h-3V5H4v1H1z M3 7h10l1.5 7h-13z M8 9a2 2 0 1 0 0.01 0z"/></svg>
        <span>0472 913 706</span>
      </li>
      <li class="contact-item">
        <svg class="contact-icon" viewBox="0 0 16 16" aria-hidden="true"><path d="M1 3h14v1.2L8 9 1 4.2z M1 6l7 4.8L15 6v7H1z"/></svg>
        <span>admin@harbourlineconstruct.com.au</span>
      </li>
      <li class="contact-item">
        <svg class="contact-icon" viewBox="0 0 16 16" aria-hidden="true"><path d="M8 1a7 7 0 1 0 0 14A7 7 0 0 0 8 1zm0 1.5a5.5 5.5 0 0 1 4.6 2.5H10l-1 2-2-1-2 2 1 3v2.2A5.5 5.5 0 0 1 8 2.5z"/></svg>
        <span>www.harbourlineconstruct.com.au</span>
      </li>
    </ul>
    <p class="address-line"><span class="company">Harbourline Construct</span> - 87 Quayside Road, Sydney, NSW 2000</p>
  </section>
</body>
</html>
```